Korvel Mining Webpage

Need a website for a copper mining company that is seeking financing and /or partners with small mines. We need a website that will give basic information regarding the property we are seeking financing for, and background information of the owners (about us), current opportunity page that will convey our value added proposition, along with a 'contact us' page.

Please review other mining companies website for ideas
Any clarity needed we will communicate with you, please ask if you are uncertain.

We will likely provide more information as the design develops

Target Market(s)

Investment companies and Mining professionals

Industry/Entity Type

Mining

Number of Pages Required

4 page

Font styles to use
Sans Serif

Colors

Designer to choose colors to be used in the design.

Requirements
Must have
• I am looking to have a template which I can use later as well to add my own content. Please be sure to have each item (designs, links buttons, drop down menus)its own file so I can import into the web formats
• Also please provide primary colors used as RGB values.
• Include a list of fonts used.
• Pages see attached power point slides
• 1) About us - what we do (2 slide of the .ppt attached) need to leave room for a mission and vision statement
• 2) current opportunities (see word document and Slide 5 as results)
• 3) Value Add ideas ( pages 3)
• 4) Management (our photos Slide 4 of the deck) with room to type background information
• 5) Events and current information (this will be a page listing dates of events, and also blog entries.)
• Let us know if you can't open a .ppt file
Nice to have
• Non-cartoonish look, it should be a polished website
• Drop down menu format
• Scrolling format with an image in the background
• Contact information page (see first slide of slide deck)
• Feel free to use the photos as needed through out the site

```html
<!DOCTYPE html>
<html lang="en">
<head>
<meta charset="utf-8">
<title>Korvel Mining</title>
<link href="https://fonts.googleapis.com/css2?family=Cinzel:wght@400;700&family=Lato:wght@400;700&display=swap" rel="stylesheet">
<style>
:root{
  --green:#10b04a;
  --green-dark:#0a9a3e;
  --red:#c8151d;
  --orange:#f5a623;
  --ink:#222;
  --grey:#666;
  --line:#d8d8d8;
  --footer:#2a2a2a;
  --white:#fff;
}
*{box-sizing:border-box;margin:0;padding:0}
html,body{width:1200px;height:3913px;overflow:hidden}
body{font-family:'Lato',sans-serif;color:var(--ink);background:var(--white);position:relative}
section,header,footer,.topbar{position:absolute;left:0;width:1200px}
.serif{font-family:'Cinzel',serif}

.topbar{top:0;height:26px;background:var(--green);color:var(--white);font-size:12px;display:flex;justify-content:flex-end;align-items:center;gap:22px;padding-right:70px}
.topbar span{display:flex;align-items:center;gap:6px}

.site-header{top:26px;height:99px;background:var(--white)}
.brand{position:absolute;left:118px;top:44px;display:flex;align-items:center;gap:10px;font-family:'Cinzel',serif;font-size:24px;color:var(--ink);letter-spacing:1px}
.brand .dot{width:14px;height:14px;border-radius:50%;background:var(--green)}
.main-nav{position:absolute;left:430px;top:58px;display:flex;font-size:14px;font-weight:700;text-transform:uppercase}
.main-nav a{color:var(--ink);text-decoration:none;padding:0 22px;border-right:1px solid var(--line)}
.main-nav a:last-child{border-right:none}
.main-nav a.active{color:var(--green)}

.hero{top:125px;height:561px}
.hero-image{position:absolute;inset:0;background:linear-gradient(180deg,#bdb8ae 0%,#8c857a 45%,#4d4a45 100%)}
.hero-caption{position:absolute;left:0;right:0;top:615px;margin-top:-125px;height:72px;background:rgba(0,0,0,.45);color:var(--white);font-family:'Cinzel',serif;font-weight:700;font-size:35px;text-align:center;line-height:72px;letter-spacing:1px}
.hero-arrow{position:absolute;top:633px;margin-top:-125px;color:var(--white);font-size:26px}

.section-title{font-family:'Cinzel',serif;font-size:31px;text-align:center;letter-spacing:1px;position:absolute;left:0;right:0}
.divider{position:absolute;left:500px;width:200px;height:14px}
.divider:before{content:"";position:absolute;left:0;right:0;top:7px;border-top:1px solid var(--line)}
.divider:after{content:"";position:absolute;left:93px;top:0;width:14px;height:14px;border-radius:50%;background:var(--ink)}
.on-green .divider:before{border-color:rgba(255,255,255,.5)}
.on-green .divider:after{background:var(--white)}

.about{top:686px;height:483px}
.about-diagram{position:absolute;left:122px;top:200px}
.read-more{position:absolute;left:552px;top:372px;color:var(--green);font-size:14px;font-weight:700;text-decoration:underline}

.solutions{top:1169px;height:521px;background:var(--green);color:var(--white)}
.solutions .section-title{top:80px;color:var(--white)}
.solutions .divider{top:130px}
.solution-row{position:absolute;left:105px;top:230px;width:990px;display:flex;justify-content:space-between}
.solution-row:before{content:"";position:absolute;left:80px;right:80px;top:62px;border-top:2px dashed rgba(255,255,255,.6)}
.solution{width:180px;text-align:center;position:relative}
.solution .icon{width:112px;height:112px;border-radius:50%;background:var(--white);margin:6px auto 0;display:flex;align-items:center;justify-content:center;border:4px solid #1b1b1b}
.solution h3{font-size:16px;font-weight:700;margin-top:40px;line-height:1.3}

.team{top:1690px;height:731px}
.team .section-title{top:78px}
.team .section-title .accent{color:var(--green)}
.team .divider{top:128px}
.member{position:absolute;top:190px;width:272px;padding:10px;}
.member.featured{border:2px solid var(--green);}
.member .photo{width:261px;height:170px;background:linear-gradient(135deg,#cfc9c2,#8d8782)}
.member h3{color:var(--red);font-size:20px;margin-top:18px}
.member .role{font-size:16px;margin-top:2px}
.member ul{margin-top:18px;border-top:1px solid var(--line);padding-top:14px;list-style:none;font-size:11px;color:var(--grey);line-height:1.45}
.member li{margin-bottom:12px;padding-left:12px;position:relative}
.member li:before{content:"";position:absolute;left:0;top:6px;width:4px;height:4px;background:var(--grey);border-radius:50%}

.band{top:2421px;height:256px;background:linear-gradient(90deg,#0d0d0d 0%,#1b1b1b 45%,#4a4a4a 75%,#1a1a1a 100%)}
.band h2{position:absolute;left:122px;top:76px;color:var(--white);font-size:26px;font-weight:700}
.band .cta{position:absolute;left:122px;top:138px;width:190px;height:50px;background:var(--green);color:var(--white);font-weight:700;font-size:15px;display:flex;align-items:center;justify-content:center}

.financials{top:2677px;height:631px}
.financials .section-title{top:78px;color:var(--green)}
.financials .section-title .dark{color:var(--ink)}
.financials .divider{top:128px}
.case{position:absolute;top:200px;width:277px}
.chart{width:277px;height:188px;border:1px solid var(--line)}
.case h3{color:var(--green);font-size:18px;margin-top:18px;padding-bottom:14px;border-bottom:1px solid var(--line)}
.case ul{list-style:none;font-size:11px;color:var(--grey);margin-top:12px;line-height:2}
.case li:before{content:"• "}

.inquiry{top:3308px;height:253px;background:var(--green);color:var(--white)}
.inquiry h2{position:absolute;left:123px;top:36px;font-family:'Cinzel',serif;font-size:34px;line-height:1.1;font-weight:400;letter-spacing:1px}
.inquiry p{position:absolute;left:123px;top:124px;width:290px;font-size:11px;line-height:1.6}
.inquiry h4{position:absolute;left:475px;top:38px;font-size:17px;font-weight:700}
.field{position:absolute;height:36px;background:var(--white);color:#888;font-size:11px;padding:12px 10px}
.send{position:absolute;left:475px;top:168px;width:133px;height:34px;background:#111;color:var(--white);font-size:13px;font-weight:700;display:flex;align-items:center;justify-content:center}

.site-footer{top:3561px;height:352px;background:var(--footer);color:var(--white)}
.contact-item{position:absolute;top:36px;text-align:center;font-size:12px}
.contact-item svg{display:block;margin:0 auto 12px}
.footer-brand{position:absolute;left:0;right:0;top:150px;text-align:center;font-family:'Cinzel',serif;font-size:26px;letter-spacing:2px}
.footer-nav{position:absolute;left:0;right:0;top:246px;display:flex;justify-content:center;font-size:13px;font-weight:700}
.footer-nav a{color:var(--white);text-decoration:none;padding:0 22px;border-right:1px solid #555}
.footer-nav a:last-child{border-right:none}
.copyright{position:absolute;left:160px;top:308px;font-size:11px;color:#ccc}
.social{position:absolute;left:876px;top:298px;display:flex;gap:12px}
.social span{width:30px;height:30px;border-radius:50%;display:block}
</style>
</head>
<body>

<div class="topbar">
  <span><svg width="12" height="12" viewBox="0 0 24 24"><path fill="#fff" d="M6.6 10.8a15 15 0 006.6 6.6l2.2-2.2c.3-.3.7-.4 1-.2 1.1.4 2.3.6 3.6.6.6 0 1 .4 1 1V20c0 .6-.4 1-1 1A17 17 0 013 4c0-.6.4-1 1-1h3.5c.6 0 1 .4 1 1 0 1.2.2 2.4.6 3.6.1.3 0 .7-.2 1z"/></svg>012-555-0148</span>
  <span><svg width="13" height="10" viewBox="0 0 26 20"><rect x="1" y="1" width="24" height="18" fill="none" stroke="#fff" stroke-width="2"/><path d="M1 1l12 10L25 1" fill="none" stroke="#fff" stroke-width="2"/></svg>dharrow@korvelmining.net</span>
</div>

<header class="site-header">
  <div class="brand"><span class="dot"></span>Korvel Mining</div>
  <nav class="main-nav">
    <a class="active">Home</a><a>About ▾</a><a>Opportunities</a><a>Our Team</a><a>Events</a><a>Contact Us</a>
  </nav>
</header>

<section class="hero">
  <div class="hero-image" role="img" aria-label="Photo of miners in helmets and safety gear in an underground meeting room"></div>
</section>
<div class="hero-caption" style="position:absolute;top:615px;margin:0">THE GREAT MINING EXPERIENCE COMPANY</div>
<div class="hero-arrow" style="left:90px;top:633px;margin:0">‹</div>
<div class="hero-arrow" style="left:1095px;top:633px;margin:0">›</div>

<section class="about">
  <h2 class="section-title" style="top:84px">About Korvel Mining</h2>
  <div class="divider" style="top:132px"></div>
  <svg class="about-diagram" width="960" height="160" viewBox="0 0 960 160" font-family="Lato,sans-serif">
    <rect x="2" y="30" width="370" height="40" fill="none" stroke="#10b04a" stroke-width="2"/>
    <text x="10" y="45" font-size="11" font-weight="700" fill="#10b04a">Form a new copper focused Mining Company</text>
    <text x="10" y="62" font-size="11" fill="#333">•  Acquire majority in small scale producing operations</text>
    <polygon points="365,2 485,2 425,90" fill="#fff" stroke="#10b04a" stroke-width="2"/>
    <text x="425" y="22" font-size="11" font-weight="700" fill="#10b04a" text-anchor="middle">Immediate</text>
    <text x="425" y="36" font-size="11" font-weight="700" fill="#10b04a" text-anchor="middle">Operating</text>
    <text x="425" y="50" font-size="11" font-weight="700" fill="#10b04a" text-anchor="middle">Cash</text>
    <text x="425" y="64" font-size="11" font-weight="700" fill="#10b04a" text-anchor="middle">Flow</text>
    <polygon points="425,150 485,40 545,150" fill="#fff" stroke="#10b04a" stroke-width="2"/>
    <text x="485" y="80" font-size="11" font-weight="700" fill="#10b04a" text-anchor="middle">High</text>
    <text x="485" y="94" font-size="11" font-weight="700" fill="#10b04a" text-anchor="middle">Probability</text>
    <text x="485" y="108" font-size="11" font-weight="700" fill="#10b04a" text-anchor="middle">for added</text>
    <text x="485" y="122" font-size="11" font-weight="700" fill="#10b04a" text-anchor="middle">Value and</text>
    <text x="485" y="136" font-size="11" font-weight="700" fill="#10b04a" text-anchor="middle">Growth</text>
    <rect x="540" y="2" width="295" height="90" fill="none" stroke="#10b04a" stroke-width="2"/>
    <text x="592" y="20" font-size="12" font-weight="700" fill="#10b04a">Targets are:</text>
    <text x="592" y="40" font-size="11" fill="#333">•  Under-capitalized</text>
    <text x="592" y="60" font-size="11" fill="#333">•  Hold numerous under-explored concessions</text>
    <text x="592" y="80" font-size="11" fill="#333">•  Located in proven mining districts</text>
  </svg>
  <a class="read-more">READ MORE &gt;&gt;</a>
</section>

<section class="solutions on-green">
  <h2 class="section-title">Our Solutions</h2>
  <div class="divider"></div>
  <div class="solution-row">
    <div class="solution"><div class="icon"><svg width="50" height="50" viewBox="0 0 50 50"><path d="M5 12h40L25 44z" fill="none" stroke="#222" stroke-width="3"/><circle cx="25" cy="20" r="5" fill="#222"/></svg></div><h3>Ownership<br>Consolidation</h3></div>
    <div class="solution"><div class="icon"><svg width="50" height="50" viewBox="0 0 50 50"><circle cx="25" cy="25" r="18" fill="none" stroke="#222" stroke-width="3"/><circle cx="25" cy="25" r="6" fill="#222"/></svg></div><h3>Management With<br>Track Record In District</h3></div>
    <div class="solution"><div class="icon"><svg width="50" height="50" viewBox="0 0 50 50"><text x="25" y="40" font-size="42" font-family="Lato,sans-serif" text-anchor="middle" fill="#222">$</text></svg></div><h3>Smart Low<br>Level Capital</h3></div>
    <div class="solution"><div class="icon"><svg width="50" height="50" viewBox="0 0 50 50"><rect x="6" y="28" width="30" height="12" fill="#222"/><path d="M30 28l12-20" stroke="#222" stroke-width="4"/><circle cx="12" cy="42" r="4" fill="#222"/><circle cx="30" cy="42" r="4" fill="#222"/></svg></div><h3>Exploration<br>Drilling</h3></div>
    <div class="solution"><div class="icon"><svg width="50" height="50" viewBox="0 0 50 50"><rect x="8" y="30" width="7" height="12" fill="#222"/><rect x="20" y="22" width="7" height="20" fill="#222"/><rect x="32" y="12" width="7" height="30" fill="#222"/><path d="M6 20l14-10 8 5 14-10" fill="none" stroke="#222" stroke-width="2"/></svg></div><h3>Increased Profits &amp;<br>Company Value</h3></div>
  </div>
</section>

<section class="team">
  <h2 class="section-title"><span class="accent">Our</span> Team</h2>
  <div class="divider"></div>
  <article class="member" style="left:128px">
    <div class="photo" role="img" aria-label="Portrait photo of Daniel Harrow"></div>
    <h3>Daniel Harrow</h3><div class="role">CEO</div>
    <ul>
      <li>13 yr mining experience</li>
      <li>Masters in Mining Engineering from Westridge School of Mines.</li>
      <li>Former General Manger Halvern Mining Calderon</li>
      <li>Proven history of UG mine production growth and reserve increases</li>
      <li>Passed all roles at Open Pit and Underground Operations: Superintendent up to General Manager</li>
    </ul>
  </article>
  <article class="member featured" style="left:462px">
    <div class="photo" role="img" aria-label="Portrait photo of Tomás Verano"></div>
    <h3>Tomás Verano</h3><div class="role">COO</div>
    <ul>
      <li>9 yr mining experience</li>
      <li>Current General Manager of Santa Irene &amp; Alcor</li>
      <li>Currently 3% owner of Las Piedras</li>
      <li>Born and raised in the district well connected</li>
    </ul>
  </article>
  <article class="member" style="left:788px">
    <div class="photo" role="img" aria-label="Portrait photo of Lucía Ferrandez"></div>
    <h3>Lucía Ferrandez</h3><div class="role">Legal Consul</div>
    <ul>
      <li>15 yr mining experience</li>
      <li>Local Counsel for Alto Sereno Project (Cerro Vidal-Quiñal)</li>
      <li>Local Counsel for Brevik Marqueza Mine</li>
      <li>Currently 6% owner of Las Piedras</li>
    </ul>
  </article>
</section>

<section class="band" role="img" aria-label="Black and white photo of miners with headlamps underground">
  <h2>THE SMALL INDEPENDENT MINING COMPANY</h2>
  <div class="cta">CONTACT US &gt;</div>
</section>

<section class="financials">
  <h2 class="section-title">Financials <span class="dark">and</span> Growth Cases</h2>
  <div class="divider"></div>
  <div class="case" style="left:146px">
    <svg class="chart" viewBox="0 0 277 188" font-family="Lato,sans-serif"><text x="138" y="20" font-size="11" font-weight="700" text-anchor="middle">NPV 8%</text><g stroke="#ddd"><line x1="40" y1="40" x2="260" y2="40"/><line x1="40" y1="80" x2="260" y2="80"/><line x1="40" y1="120" x2="260" y2="120"/><line x1="40" y1="158" x2="260" y2="158"/></g><rect x="62" y="150" width="16" height="8" fill="#c8151d"/><rect x="80" y="138" width="16" height="20" fill="#f5a623"/><rect x="132" y="150" width="16" height="8" fill="#c8151d"/><rect x="150" y="128" width="16" height="30" fill="#f5a623"/><rect x="202" y="138" width="16" height="20" fill="#c8151d"/><rect x="220" y="70" width="16" height="88" fill="#f5a623"/><text x="80" y="172" font-size="9" text-anchor="middle">Base Case</text><text x="150" y="172" font-size="9" text-anchor="middle">Case 1</text><text x="220" y="172" font-size="9" text-anchor="middle">Case 2</text></svg>
    <h3>Base Case Op Improvements</h3>
    <ul><li>Operational Improvements</li><li>Open increase, hire mine and plant managers</li><li>Increase head grade &amp; mill inc.</li><li>Capex = $4M (purchase price)</li></ul>
  </div>
  <div class="case" style="left:464px">
    <svg class="chart" viewBox="0 0 277 188" font-family="Lato,sans-serif"><text x="138" y="20" font-size="11" font-weight="700" text-anchor="middle">NPV 8%</text><g stroke="#ddd"><line x1="40" y1="40" x2="260" y2="40"/><line x1="40" y1="80" x2="260" y2="80"/><line x1="40" y1="120" x2="260" y2="120"/><line x1="40" y1="158" x2="260" y2="158"/></g><rect x="62" y="150" width="16" height="8" fill="#c8151d"/><rect x="80" y="138" width="16" height="20" fill="#f5a623"/><rect x="132" y="150" width="16" height="8" fill="#c8151d"/><rect x="150" y="128" width="16" height="30" fill="#f5a623"/><rect x="202" y="138" width="16" height="20" fill="#c8151d"/><rect x="220" y="70" width="16" height="88" fill="#f5a623"/><text x="80" y="172" font-size="9" text-anchor="middle">Base Case</text><text x="150" y="172" font-size="9" text-anchor="middle">Case 1</text><text x="220" y="172" font-size="9" text-anchor="middle">Case 2</text></svg>
    <h3>Case 1: Mill + Exploration</h3>
    <ul><li>Base Case operational improvements</li><li>Plant (12.5 kt/month to 17 kt/m)</li><li>Exploration drilling (10,000m)</li><li>Capex = $6.4M (incl. purchase)</li></ul>
  </div>
  <div class="case" style="left:783px">
    <svg class="chart" viewBox="0 0 277 188" font-family="Lato,sans-serif"><text x="138" y="20" font-size="11" font-weight="700" text-anchor="middle">NPV 8%</text><g stroke="#ddd"><line x1="40" y1="40" x2="260" y2="40"/><line x1="40" y1="80" x2="260" y2="80"/><line x1="40" y1="120" x2="260" y2="120"/><line x1="40" y1="158" x2="260" y2="158"/></g><rect x="62" y="150" width="16" height="8" fill="#c8151d"/><rect x="80" y="138" width="16" height="20" fill="#f5a623"/><rect x="132" y="150" width="16" height="8" fill="#c8151d"/><rect x="150" y="128" width="16" height="30" fill="#f5a623"/><rect x="202" y="138" width="16" height="20" fill="#c8151d"/><rect x="220" y="70" width="16" height="88" fill="#f5a623"/><text x="80" y="172" font-size="9" text-anchor="middle">Base Case</text><text x="150" y="172" font-size="9" text-anchor="middle">Case 1</text><text x="220" y="172" font-size="9" text-anchor="middle">Case 2</text></svg>
    <h3>Mill + Exploration + Mine Development</h3>
    <ul><li>Base Case operational improvements</li><li>Plant (12.5 kt/month to 17 kt/m)</li><li>Exploration drilling (10,000m)</li><li>Capex = $6.4M (incl. purchase)</li></ul>
  </div>
</section>

<section class="inquiry">
  <h2>Quick<br>Inquiry</h2>
  <p>Send us a short note about your project, your mine or your interest in partnering, and our team will reply within two business days with next steps... [+]</p>
  <h4>Please fill up bellow form</h4>
  <div class="field" style="left:475px;top:76px;width:272px">Name</div>
  <div class="field" style="left:767px;top:76px;width:272px">Email</div>
  <div class="field" style="left:475px;top:124px;width:272px">Phone</div>
  <div class="field" style="left:767px;top:124px;width:272px">Message</div>
  <div class="send">READ MORE ▸</div>
</section>

<footer class="site-footer">
  <div class="contact-item" style="left:130px;width:262px"><svg width="18" height="24" viewBox="0 0 18 24"><path d="M9 1a8 8 0 018 8c0 6-8 14-8 14S1 15 1 9a8 8 0 018-8z" fill="none" stroke="#fff" stroke-width="1.5"/><circle cx="9" cy="9" r="3" fill="#fff"/></svg>123, Lorem Ipsum Street Name, City Name 01245</div>
  <div class="contact-item" style="left:474px;width:200px"><svg width="22" height="22" viewBox="0 0 24 24"><path fill="none" stroke="#fff" stroke-width="1.5" d="M6.6 10.8a15 15 0 006.6 6.6l2.2-2.2c.3-.3.7-.4 1-.2 1.1.4 2.3.6 3.6.6.6 0 1 .4 1 1V20c0 .6-.4 1-1 1A17 17 0 013 4c0-.6.4-1 1-1h3.5c.6 0 1 .4 1 1 0 1.2.2 2.4.6 3.6.1.3 0 .7-.2 1z"/></svg>Phone: 012-555-0148</div>
  <div class="contact-item" style="left:810px;width:250px"><svg width="22" height="22" viewBox="0 0 24 24"><path d="M2 11L22 2l-7 20-3-8z" fill="none" stroke="#fff" stroke-width="1.5"/></svg>Email: dharrow@korvelmining.net</div>
  <div class="footer-brand">Korvel Mining</div>
  <nav class="footer-nav"><a>HOME</a><a>ABOUT</a><a>OPPORTUNITIES</a><a>OUR TEAM</a><a>EVENTS</a><a>CONTACT US</a></nav>
  <div class="copyright">Copyright © 2019 Korvel Mining. All Right Reserved</div>
  <div class="social"><span style="background:#3b5a9a"></span><span style="background:#0a77b5"></span><span style="background:#2aa3ef"></span><span style="background:#d9482f"></span></div>
</footer>

</body>
</html>
```